Business Card: RW Office Partners - Your organised problem solver

Business Name: RW Office Partners
Website: www.rwofficepartners-example.com.au
Email: maribel@rwofficepartners-example.com.au
Mobile: 61 400 000 000
Facebook: @rwofficepartners
Instrgram: @rwofficepartners

Brading Colours:
HEX
#986474
#ddccd3
#7a8498
#c9d8e4
#000000
#ffffff

Tag Line: Your organised problem solver

Link to DRAFT website:
https://draftsites-example.com/rw-office-partners

About Page from the website:
My name is Maribel Rowe, and I would love to assist you to become more productive in your day to day and achieve your business and personal goals.
My mission is to give you time, time to work on the important tasks of your business or to be able to spend more time with your family. I will take on the tasks you don’t have time for, don’t know well or simply don’t like to do.
I have an extensive background in Administration, Tender Coordination, Document Control, WHS and Quality Management working primarily in the Construction, Mining and Corporate World.
I am passionate about being organised, having order and making things in your life (and mine) easier! I love to watch something unfold and grow into something amazing! I am known for being the go-to problem solver, the organiser of all things, producing high standards of work even under pressure. I’m also a confident communicator, and I understand that you’re busy running your business.

Target Market(s)

Small to Medium Business who require assistance in their business by a virtual assistant.

Industry/Entity Type

Virtual Assistant

Contact Information for Business Card

Mobile: 61 400 000 000

Font styles to use
Sans Serif

Colors
ffffff

Requirements
Must have
• Branding Colours as outlined.
Contact Details as outlined.
Logo as provided.
Proper contact details - mobile, facebook, instragm, website.
Simple, Elegant, very clean looking.
Should not have
• Note cute with pictures.
Not too girly as still want to market to construction companies.

```html
<!DOCTYPE html>
<html lang="en">
<head>
<meta charset="UTF-8">
<title>RW Office Partners – Business Card</title>
<link href="https://fonts.googleapis.com/css2?family=Montserrat:wght@400;500;600;700&display=swap" rel="stylesheet">
<style>
  :root {
    --mauve: #986474;
    --mauve-light: #ddccd3;
    --slate: #7a8498;
    --sky: #c9d8e4;
    --ink: #000000;
    --paper: #ffffff;
    --stage: #2b2b2d;
  }
  * { margin: 0; padding: 0; box-sizing: border-box; }
  html, body { width: 1200px; height: 900px; overflow: hidden; }
  body {
    background: var(--stage);
    font-family: "Montserrat", Arial, sans-serif;
    display: flex;
    flex-direction: column;
    align-items: center;
    justify-content: center;
    gap: 50px;
  }
  .card {
    position: relative;
    width: 665px;
    height: 380px;
    overflow: hidden;
  }

  /* Back of card */
  .card-back { background: var(--mauve); color: var(--paper); }
  .card-back .brand {
    position: absolute;
    left: 0; right: 0; top: 145px;
    text-align: center;
    font-size: 40px;
    font-weight: 600;
    letter-spacing: 1px;
  }
  .card-back .site {
    position: absolute;
    left: 0; right: 0; bottom: 48px;
    text-align: center;
    font-size: 14px;
    font-weight: 500;
    letter-spacing: 2px;
    text-transform: uppercase;
  }

  /* Front of card */
  .card-front { background: var(--paper); }
  .card-front .brand {
    position: absolute;
    right: 40px; top: 70px;
    font-size: 30px;
    font-weight: 600;
    color: var(--mauve);
    letter-spacing: 0.5px;
  }
  .person { position: absolute; left: 40px; top: 60px; }
  .person-name {
    font-size: 21px;
    font-weight: 700;
    color: var(--slate);
    letter-spacing: 1px;
    text-transform: uppercase;
  }
  .person-role {
    margin-top: 4px;
    font-size: 15px;
    font-weight: 500;
    color: var(--mauve);
  }
  .contacts {
    position: absolute;
    left: 40px; bottom: 42px;
    list-style: none;
  }
  .contacts li {
    display: flex;
    align-items: center;
    gap: 12px;
    height: 25px;
    font-size: 15px;
    color: var(--slate);
  }
  .contacts svg { width: 16px; height: 16px; flex: none; }
  .footer-band { position: absolute; left: 0; bottom: 0; }
  .tagline {
    position: absolute;
    left: 412px; bottom: 17px;
    font-size: 11px;
    font-weight: 700;
    letter-spacing: 1.2px;
    color: var(--paper);
    text-transform: uppercase;
  }
</style>
</head>
<body>

<section class="card card-back">
  <div class="brand">RW Office Partners</div>
  <div class="site">www.rwofficepartners-example.com.au</div>
</section>

<section class="card card-front">
  <div class="person">
    <div class="person-name">Your Name Here</div>
    <div class="person-role">Managing Director</div>
  </div>

  <div class="brand">RW Office Partners</div>

  <ul class="contacts">
    <li>
      <svg viewBox="0 0 16 16" aria-hidden="true"><rect x="4" y="1" width="8" height="14" rx="1.5" fill="none" stroke="var(--mauve)" stroke-width="1.6"/><rect x="6" y="9" width="4" height="3" fill="var(--mauve)"/></svg>
      61 400 000 000
    </li>
    <li>
      <svg viewBox="0 0 16 16" aria-hidden="true"><rect x="1" y="3" width="14" height="10" fill="var(--mauve)"/><path d="M1 3 L8 9 L15 3" fill="none" stroke="var(--paper)" stroke-width="1.2"/></svg>
      maribel@rwofficepartners-example.com.au
    </li>
    <li>
      <svg viewBox="0 0 16 16" aria-hidden="true"><circle cx="8" cy="8" r="6.5" fill="none" stroke="var(--mauve)" stroke-width="1.4"/><ellipse cx="8" cy="8" rx="3" ry="6.5" fill="none" stroke="var(--mauve)" stroke-width="1.2"/><line x1="1.5" y1="8" x2="14.5" y2="8" stroke="var(--mauve)" stroke-width="1.2"/></svg>
      www.rwofficepartners
    </li>
    <li>
      <svg viewBox="0 0 16 16" aria-hidden="true"><circle cx="8" cy="8" r="6.5" fill="none" stroke="var(--mauve)" stroke-width="1.8"/></svg>
      rwofficepartners
    </li>
    <li>
      <svg viewBox="0 0 16 16" aria-hidden="true"><rect x="2" y="2" width="12" height="12" fill="var(--mauve)"/></svg>
      @rwofficepartners
    </li>
  </ul>

  <svg class="footer-band" width="665" height="48" viewBox="0 0 665 48" aria-hidden="true">
    <polygon points="0,30 380,30 402,0 665,0 665,48 0,48" fill="var(--mauve)"/>
  </svg>
  <div class="tagline">Your organised problem solver</div>
</section>

</body>
</html>
```